Business Card Design for Mabel's Pantry

We make food for dogs.
Business Card Design (using the logo designed by you). Our Brand color is a bright canary yellow. For example our signage is predominantly yellow, with the logo in black. I'd like the card also to use that imagery.
Feel free to use the two sides creatively.
Vertical Design is also great.

Industry/Entity Type

Pet food

Contact Information for Business Card

Name, email, website, phone no

Font styles to use
Sans Serif

Colors
59FF00
82FF00
B8FF75
E3FFCB
F4FFEA
FFF300
FFF600
FEFA6F
FFFEC7
FFFEE8

Requirements
Nice to have
• A graphic in the same brush stroke style of the logo shoeing a doggy bowl of food

```html
<!DOCTYPE html>
<html lang="en">
<head>
<meta charset="utf-8">
<title>Mabel's Pantry – Business Card</title>
<link href="https://fonts.googleapis.com/css2?family=Oswald:wght@400&family=Open+Sans:wght@400;700&display=swap" rel="stylesheet">
<style>
  :root {
    --canary: #fde256;
    --ink: #141414;
    --charcoal: #1b1c1e;
    --stage: #d9d9d6;
    --logo-yellow: #f5df3a;
  }
  html, body {
    margin: 0;
    width: 1200px;
    height: 1108px;
    overflow: hidden;
    background: var(--stage);
  }
  .sheet {
    position: relative;
    width: 1200px;
    height: 1108px;
    display: flex;
    justify-content: center;
    align-items: center;
    gap: 60px;
  }
  .card {
    width: 360px;
    height: 580px;
    border-radius: 26px;
    position: relative;
    box-sizing: border-box;
    box-shadow: 0 10px 30px rgba(0,0,0,.18);
  }
  .card--front { background: var(--canary); color: var(--ink); }
  .card--back { background: var(--charcoal); color: var(--logo-yellow); }
  .brand {
    position: absolute;
    left: 0; right: 0;
    text-align: center;
    font-family: 'Oswald', sans-serif;
    font-weight: 400;
    font-size: 40px;
    line-height: 1;
    letter-spacing: .5px;
    text-transform: uppercase;
    white-space: nowrap;
  }
  .card--front .brand { top: 140px; }
  .card--back .brand { top: 270px; }
  .person {
    position: absolute;
    left: 40px;
    right: 30px;
    top: 318px;
    font-family: 'Open Sans', sans-serif;
  }
  .person__name { font-weight: 700; font-size: 30px; margin: 0; line-height: 1.1; text-transform: uppercase; white-space: nowrap; }
  .person__role { font-size: 18px; margin: 2px 0 18px; }
  .contact { list-style: none; padding: 0; margin: 0; font-size: 14px; }
  .contact li { display: flex; align-items: center; gap: 10px; margin-bottom: 9px; white-space: nowrap; }
  .contact svg { width: 20px; height: 20px; flex: none; }
  .address { font-size: 15px; margin-top: 10px; line-height: 1.35; }
</style>
</head>
<body>
<main class="sheet">
  <section class="card card--front">
    <div class="brand">Mabel's Pantry</div>
    <div class="person">
      <h1 class="person__name">Tessa Quillmore</h1>
      <p class="person__role">Manager</p>
      <ul class="contact">
        <li><svg viewBox="0 0 20 20"><rect width="20" height="20" rx="3" fill="#141414"/><path d="M6 5c1 0 1.5 2 1.5 2.5S6.5 8.5 7 9.5s2 2.5 3 3 1.5-1 2-1 2.5.5 2.5 1.5-1 2-2 2C8 15 5 12 5 8c0-1.5 0-3 1-3z" fill="#fde256"/></svg>555-013-2847</li>
        <li><svg viewBox="0 0 20 20"><rect width="20" height="20" rx="3" fill="#141414"/><rect x="4" y="6" width="12" height="8" fill="none" stroke="#fde256" stroke-width="1.4"/><path d="M4 6l6 5 6-5" fill="none" stroke="#fde256" stroke-width="1.4"/></svg>hello@mabelspantry.com</li>
        <li><svg viewBox="0 0 20 20"><rect width="20" height="20" rx="3" fill="#141414"/><circle cx="10" cy="10" r="6" fill="none" stroke="#fde256" stroke-width="1.3"/><path d="M4 10h12M10 4v12M10 4c-3 3-3 9 0 12M10 4c3 3 3 9 0 12" fill="none" stroke="#fde256" stroke-width="1"/></svg>www.mabelspantry.com</li>
      </ul>
      <div class="address">88 Orchard Row, Suite 4<br>Maple Falls, ST 0000</div>
    </div>
  </section>
  <section class="card card--back">
    <div class="brand">Mabel's Pantry</div>
  </section>
</main>
</body>
</html>
```